Book cover for The Quiet Lioness Manual to Turn into a Powerhouse at Work

Book cover design for soft cover non-fiction book.

The front cover is what is most important at this stage, I am still gathering the testimonials and book description for the back cover so a rough to be completed later for the back is great.

Title as per above. Divided up "The Quiet Lioness Manual" (to be a series) and "Turn into a Powerhouse at Work" in this book in the series

Also for the front:

Lorna Kevesh

"The most unusual business book you will read." - Gwen Talrowicz, Author of Founder Sunrise

Background info:

This work is a blending of the masculine and feminine energies, the practical business skills with a strong focus on the inner game. I am looking for the cover to have a nod to the Dominatrix and a clear message that one can be soft (kind, open hearted) and still be strong and firm in business.

Photo options are in this file https://www.filecrate-example.net/sh/qmx41tgbw8vkrle/BBEtmkqpQ2XrLm3nXoyy94J4b?dl=0

Size 6" x 9" 179 pgs

Target Market(s)

female entreprenures

Industry/Entity Type

Business

Colors

Designer to choose colors to be used in the design.

Requirements
Must have
• I would like the title to be in a font that is bold and upscale, to contrast the softness fo the image.
• Clear and readable
• Unique look that will stand out
Should not have
• overt Dominatrix images or slant. It is about the energy not the actual.

```html
<!DOCTYPE html>
<html lang="en">
<head>
<meta charset="utf-8">
<title>Quiet Lioness — Book Cover Wrap</title>
<link rel="stylesheet" href="https://fonts.googleapis.com/css2?family=Cinzel:wght@700&family=Roboto:wght@300&display=swap">
<style>
  :root {
    --stage: #b1b437;
    --cover-top: #0e1015;
    --cover-mid: #222d45;
    --cover-bottom: #4b6192;
    --photo-dark: #3b2f35;
    --photo-red: #8f3a40;
    --photo-deep: #4a3a44;
    --ink: #ffffff;
    --ink-soft: #e9edf5;
    --serif: "Cinzel", "Copperplate", serif;
    --sans: "Roboto", "Helvetica Neue", sans-serif;
  }
  * { box-sizing: border-box; margin: 0; padding: 0; }
  html, body { width: 1200px; height: 1200px; overflow: hidden; }
  body { background: var(--stage); position: relative; }

  .cover-wrap {
    position: absolute; left: 86px; top: 289px;
    width: 1031px; height: 713px;
    background: linear-gradient(180deg, var(--cover-top) 0%, var(--cover-mid) 40%, var(--cover-bottom) 100%);
    color: var(--ink);
    overflow: hidden;
  }
  .abs { position: absolute; }
  .caps { font-family: var(--serif); font-weight: 700; text-transform: uppercase; }

  /* Back cover */
  .back-title { left: 30px; top: 54px; font-size: 50px; line-height: 1; white-space: nowrap; }
  .back-blurb { left: 30px; top: 122px; width: 402px; font-size: 10.2px; line-height: 16px; }
  .author-photo { left: 26px; top: 225px; width: 233px; height: 294px;
    background: linear-gradient(180deg, #8a93a3 0%, #b7bcc4 30%, #7f8a95 50%, #a9a7a0 80%, #8d877d 100%); }
  .back-author { left: 28px; top: 532px; font-size: 19px; letter-spacing: .5px; }
  .back-bio { left: 30px; top: 565px; width: 390px; font-size: 10.6px; line-height: 16px; }

  /* Spine */
  .spine-text { writing-mode: vertical-rl; line-height: 1; letter-spacing: 1px; }
  .spine-title { left: 491px; top: 55px; font-size: 24px; }
  .spine-author { left: 494px; top: 491px; font-size: 19px; }

  /* Front cover */
  .cover-photo { left: 760px; top: 239px; width: 271px; height: 474px;
    background: linear-gradient(180deg, var(--photo-dark) 0%, var(--photo-red) 45%, var(--photo-deep) 100%); }
  .front-title { left: 582px; top: 62px; font-size: 50px; line-height: 1; white-space: nowrap; }
  .series { left: 584px; top: 120px; font-family: var(--sans); font-weight: 300; font-size: 26px; color: var(--ink-soft); white-space: nowrap; }
  .lead-in { left: 582px; top: 204px; font-family: var(--sans); font-weight: 300; font-size: 20px; color: var(--ink-soft); }
  .headline { left: 580px; top: 232px; font-family: var(--sans); font-weight: 300; font-size: 45px; line-height: 44px; text-transform: uppercase; }
  .front-author { left: 578px; top: 580px; font-size: 19px; letter-spacing: .5px; }
  .endorsement { left: 578px; top: 606px; font-size: 10.4px; white-space: nowrap; }
  .endorser { left: 578px; top: 631px; font-size: 19px; letter-spacing: .5px; }
  .endorser-credit { left: 578px; top: 656px; font-size: 10.4px; white-space: nowrap; }
</style>
</head>
<body>
  <main class="cover-wrap">
    <section class="back-cover">
      <h2 class="abs caps back-title">Quiet Lioness</h2>
      <p class="abs caps back-blurb">This work is a blending of the masculine and feminine energies, the practical business skills with a strong focus on the inner game. I am looking for the cover to have a nod to the Dominatrix and a clear message that one can be soft (kind, open hearted) and still be strong and firm in business.</p>
      <div class="abs author-photo" role="img" aria-label="Author portrait: woman in a turquoise sweater and white trousers standing barefoot on a shoreline under a cloudy sky"></div>
      <h3 class="abs caps back-author">Lorna Kevesh</h3>
      <p class="abs caps back-bio">Lorem ipsum dolor sit amet, consectetur adipiscing elit, sed do eiusmod tempor incididunt ut labore et dolore magna aliqua.<br>Lorem ipsum dolor sit amet, consectetur adipiscing elit, sed do eiusmod tempor incididunt ut labore et dolore magna aliqua.</p>
    </section>

    <section class="spine">
      <span class="abs caps spine-text spine-title">Quiet Lioness</span>
      <span class="abs caps spine-text spine-author">Lorna Kevesh</span>
    </section>

    <section class="front-cover">
      <div class="abs cover-photo" role="img" aria-label="Cover photo: young woman in a red plaid shirt raising red boxing gloves in a guard pose"></div>
      <h1 class="abs caps front-title">Quiet Lioness</h1>
      <p class="abs series">The Quiet Lioness Manual</p>
      <p class="abs lead-in">Turn into a</p>
      <p class="abs headline">Powerhouse<br>at<br>Work</p>
      <h3 class="abs caps front-author">Lorna Kevesh</h3>
      <p class="abs caps endorsement">The most unusual business book you will read.</p>
      <h3 class="abs caps endorser">Gwen Talrowicz</h3>
      <p class="abs caps endorser-credit">Author of Founder Sunrise</p>
    </section>
  </main>
</body>
</html>
```